" O INSTITUTO TERAVUNDA foi idealizado a partir de um ideal de auxílio humanitário a famílias (com algum idoso) com condições de sobrevivência comprometidas devido a problemas de doença, seja ela física; psicológica ou mesmo social. “ Teravunda” significa “dono da coragem” e, apesar de seu principal mantenedor ser uma casa de culto de matriz africana (Dasilore Mitaku Fenjo Arupe),o Centro Cultural visa atender a famílias com idosos que estejam desestruturadas, devido a algum tipo de doença, indiferente a visão política, religiosa e/ou cultural. Acreditamos que o idoso incluído num contexto familiar, ou mesmo num asilo, não deve ser culpado por qualquer atitude de sua juventude. Quem de nós, em idade de produção e escolhas pode garantir estar tomando decisões acertadas para seu futuro? Normalmente são as doenças que comprometem o bem estar social: vícios em bebidas e/ou drogas; doenças patológicas e/ou psicológicas ou mesmo “doenças sociais” desestruturam as relações interpessoais afastando os idosos da realidade. "

```html
<!DOCTYPE html>
<html lang="pt-BR">
<head>
<meta charset="UTF-8">
<title>Instituto Teravunda – Cadastro de Doação</title>
<link href="https://fonts.googleapis.com/css2?family=Lato:ital,wght@0,400;0,700;1,400&display=swap" rel="stylesheet">
<style>
  :root {
    --page-bg: #ffffff;
    --ink: #3a3a3a;
    --muted: #8a8a8a;
    --faint: #d4d4d4;
    --accent: #e4572e;
    --accent-soft: #eab6a2;
    --rule: #dcdcdc;
  }
  html, body {
    margin: 0;
    width: 1200px;
    height: 1200px;
    overflow: hidden;
    background: var(--page-bg);
    font-family: "Lato", sans-serif;
    color: var(--ink);
  }
  .signup-page {
    position: relative;
    width: 1200px;
    height: 1200px;
    box-sizing: border-box;
    padding: 150px 130px 0 130px;
  }
  .signup-type__title {
    margin: 0 0 18px;
    font-size: 30px;
    font-weight: 700;
    color: var(--ink);
  }
  .signup-type__options {
    display: flex;
    gap: 12px;
  }
  .type-button {
    width: 96px;
    height: 28px;
    font: 400 13px "Lato", sans-serif;
    border: 1px solid var(--accent);
    background: #fff;
    color: var(--accent);
  }
  .type-button--active {
    background: var(--accent);
    color: #fff;
  }
  .section-rule {
    border: 0;
    border-top: 1px solid var(--rule);
    margin: 22px 0 26px;
    width: 740px;
  }
  .donation__title {
    margin: 0 0 10px;
    font-size: 32px;
    font-weight: 700;
    color: var(--accent);
  }
  .donation__intro {
    margin: 0 0 26px;
    font-size: 14px;
    line-height: 1.55;
    color: var(--muted);
    font-style: italic;
    width: 760px;
  }
  .donation__body {
    display: flex;
    gap: 60px;
  }
  .donor-fields {
    display: grid;
    grid-template-columns: 230px 230px;
    gap: 12px 14px;
  }
  .text-field {
    height: 32px;
    box-sizing: border-box;
    border: 1px solid var(--accent-soft);
    padding: 0 10px;
    font: 400 13px "Lato", sans-serif;
    color: var(--muted);
    display: flex;
    align-items: center;
  }
  .contact-note {
    padding-top: 4px;
    font-size: 14px;
    line-height: 1.7;
    color: var(--faint);
  }
  .contact-note p { margin: 0 0 14px; }
  .donation-kind {
    display: flex;
    align-items: center;
    gap: 22px;
    margin: 24px 0 26px;
    font-size: 13px;
    color: var(--muted);
  }
  .donation-kind__option {
    display: flex;
    align-items: center;
    gap: 7px;
    color: var(--ink);
  }
  .donation-amount .text-field { width: 200px; }
  .donation-amount__hint {
    margin: 8px 0 0;
    font-size: 13px;
    color: var(--muted);
  }
  .submit-button {
    margin-top: 34px;
    width: 84px;
    height: 28px;
    border: 0;
    background: var(--accent);
    color: #fff;
    font: 400 13px "Lato", sans-serif;
  }
</style>
</head>
<body>
<main class="signup-page">
  <section class="signup-type">
    <h1 class="signup-type__title">Escolha qual o tipo de cadastro:</h1>
    <div class="signup-type__options">
      <button class="type-button type-button--active">Doação</button>
      <button class="type-button">Voluntariado</button>
    </div>
  </section>

  <hr class="section-rule">

  <section class="donation">
    <h2 class="donation__title">Doação</h2>
    <p class="donation__intro">Com parte do nosso tempo queremos a chance de trazer mais um idoso de volta à vida e estabilizar sua família.<br>
    Conforme você informou os dados do seu “cliente” mais um idoso será assistido por nosso Centro Cultural.</p>

    <div class="donation__body">
      <div class="donor-fields">
        <div class="text-field">Nome</div>
        <div class="text-field">Aniversário</div>
        <div class="text-field">Empresa</div>
        <div class="text-field">E-mail</div>
        <div class="text-field">Endereço</div>
        <div class="text-field">Número</div>
        <div class="text-field">Complemento</div>
        <div class="text-field">CEP</div>
        <div class="text-field">Estado</div>
        <div class="text-field">Cidade</div>
        <div class="text-field">DDD+Telefone</div>
        <div class="text-field">DDD+Celular</div>
      </div>
      <aside class="contact-note">
        <p>Centro Cultural Teravunda</p>
        <p>Rua das Acácias, 214<br>Vila Serena – SP<br>Tel. (11) 4000-2718</p>
      </aside>
    </div>

    <div class="donation-kind">
      <span>Escolha um tipo de doação:</span>
      <span class="donation-kind__option">
        <svg width="13" height="13" viewBox="0 0 13 13"><rect x="0.5" y="0.5" width="12" height="12" fill="none" stroke="#e4572e"/></svg>
        Doação única
      </span>
      <span class="donation-kind__option">
        <svg width="13" height="13" viewBox="0 0 13 13"><rect x="0.5" y="0.5" width="12" height="12" fill="none" stroke="#e4572e"/><rect x="3" y="3" width="7" height="7" fill="#e4572e"/></svg>
        Doação Mensal
      </span>
    </div>

    <div class="donation-amount">
      <div class="text-field">Valor</div>
      <p class="donation-amount__hint">Mínimo R$ 10,00</p>
    </div>

    <button class="submit-button">Enviar</button>
  </section>
</main>
</body>
</html>
```